Nine Dawns and Four Decades Book Cover Design

I need a book cover design for a book that I am writing, called "Nine Dawns and Four Decades: The Dash and Endurance Path of Reaching Peak Results".

I have attached the Table of Contents and the first Introduction Chapter of the book, to provide more context on what the book is about.

The stories in the book primarily rely on my experience of running SkyVela Q, a long-haul low-cost airline. I use "sprint and marathon" because I'm a marathon runner and ironman triathlete, and its part of my identity.

I would love a design that captures a stylized combination of an aircraft taking off, and a person running. I have attached a photo of an SkyVela Q Corvane K740 aircraft (its different from SkyVela planes because of the "X" paint strokes on the tail of the plane. Ideally, if a stylized version of the X appears on the tail, that would be great, but without the "SkyVela" text.

Generally, the cover should convey "speed", and "curiosity".

Target Market(s)

Business Book Readers in Asia

Font styles to use
Sans Serif

Colors

Designer to choose colors to be used in the design.

Requirements
Must have
• Text in the Cover from the attached file
Nice to have
• Aircraft taking off and someone running
Should not have
• "SkyVela" name/text.

```html
<!DOCTYPE html>
<html lang="en">
<head>
<meta charset="utf-8">
<title>Nine Dawns and Four Decades – Cover Spread</title>
<link href="https://fonts.googleapis.com/css2?family=Barlow+Condensed:ital,wght@1,800&family=Bebas+Neue&family=Open+Sans:wght@400&display=swap" rel="stylesheet">
<style>
  :root {
    --page-bg: #efefef;
    --sage: #b2cfb1;
    --paper: #ffffff;
    --sun: #ffd02f;
    --plum: #9b2a5a;
    --rose: #c45b6c;
    --ink: #1f1f1f;
    --body-ink: #2a2a2a;
    --splash-a: #f2607a;
    --splash-b: #ff9a3c;
    --splash-c: #a02a63;
  }
  html, body {
    margin: 0;
    width: 899px;
    height: 1200px;
    overflow: hidden;
    background: var(--page-bg);
  }
  .stage {
    position: relative;
    width: 899px;
    height: 1200px;
  }
  .spread {
    position: absolute;
    left: 20px;
    top: 302px;
    width: 1095px;
    height: 758px;
    transform: scale(0.785);
    transform-origin: 0 0;
    background: var(--sage);
    overflow: hidden;
  }
  .spread-art {
    position: absolute;
    inset: 0;
    width: 1095px;
    height: 758px;
  }
  .back-blurb {
    position: absolute;
    left: 46px;
    top: 36px;
    width: 417px;
    font-family: "Open Sans", sans-serif;
    font-size: 12.3px;
    line-height: 14.2px;
    color: var(--body-ink);
    text-align: justify;
    hyphens: auto;
  }
  .back-blurb p { margin: 0 0 14px; }
  .barcode-space {
    position: absolute;
    left: 40px;
    top: 640px;
    width: 109px;
    height: 71px;
    background: var(--paper);
  }
  .spine {
    position: absolute;
    left: 512px;
    top: 290px;
    width: 90px;
    height: 400px;
  }
  .spine-title, .spine-author {
    position: absolute;
    left: 45px;
    transform-origin: 0 0;
    transform: rotate(90deg);
    white-space: nowrap;
  }
  .spine-title {
    top: 6px;
    font-family: "Barlow Condensed", sans-serif;
    font-style: italic;
    font-weight: 800;
    font-size: 30px;
    line-height: 30px;
    margin-left: 32px;
  }
  .spine-title .line-one { color: var(--plum); display: block; }
  .spine-title .line-two { color: var(--rose); display: block; }
  .spine-author {
    top: 244px;
    margin-left: 12px;
    font-family: "Bebas Neue", sans-serif;
    font-size: 24px;
    letter-spacing: 3px;
    color: var(--plum);
  }
  .front-title {
    position: absolute;
    left: 606px;
    top: 30px;
    width: 470px;
    margin: 0;
    font-family: "Barlow Condensed", sans-serif;
    font-style: italic;
    font-weight: 800;
    text-transform: uppercase;
    text-align: center;
    white-space: nowrap;
  }
  .front-title .line-one {
    display: block;
    font-size: 76px;
    line-height: 82px;
    color: var(--plum);
  }
  .front-title .line-two {
    display: block;
    font-size: 84px;
    line-height: 92px;
    color: var(--rose);
  }
  .front-subtitle {
    position: absolute;
    left: 606px;
    top: 226px;
    width: 470px;
    margin: 0;
    font-family: "Bebas Neue", sans-serif;
    font-size: 25px;
    line-height: 30px;
    color: var(--ink);
    text-align: center;
    text-transform: uppercase;
  }
  .front-author {
    position: absolute;
    left: 606px;
    top: 684px;
    width: 470px;
    margin: 0;
    font-family: "Bebas Neue", sans-serif;
    font-size: 50px;
    line-height: 52px;
    letter-spacing: 5px;
    color: var(--plum);
    text-align: center;
    white-space: nowrap;
  }
</style>
</head>
<body>
<div class="stage">
  <div class="spread">
    <svg class="spread-art" viewBox="0 0 1095 758" xmlns="http://www.w3.org/2000/svg">
      <defs>
        <linearGradient id="splash-runner" x1="0" y1="0" x2="0.4" y2="1">
          <stop offset="0" stop-color="#ff9a3c"/>
          <stop offset="0.5" stop-color="#f2607a"/>
          <stop offset="1" stop-color="#a02a63"/>
        </linearGradient>
        <linearGradient id="splash-plane" x1="1" y1="0" x2="0" y2="1">
          <stop offset="0" stop-color="#a02a63"/>
          <stop offset="0.45" stop-color="#f2607a"/>
          <stop offset="1" stop-color="#ff9a3c"/>
        </linearGradient>
      </defs>
      <path class="paper-sweep" d="M215,0 Q400,240 600,300 Q840,360 1095,292 L1095,0 Z" fill="#ffffff"/>
      <path class="track-swoosh" d="M592,590 Q610,520 760,490 L780,505 Q660,535 655,590 Q665,650 850,665 Q980,670 1095,640 L1095,758 L990,758 Q760,740 640,680 Q590,640 592,590 Z" fill="#ffd02f"/>
      <rect class="runner-art" role="img" aria-label="Paint-splash illustration of a sprinting runner" x="760" y="310" width="300" height="350" rx="70" fill="url(#splash-runner)" opacity="0.9"/>
      <rect class="plane-art" role="img" aria-label="Paint-splash illustration of an aircraft taking off with an X on its tail" x="0" y="380" width="460" height="378" rx="90" fill="url(#splash-plane)" opacity="0.9"/>
    </svg>

    <div class="back-blurb">
      <p>Lorem ipsum dolor sit amet, consectetur adipiscing elit. Vestibulum leo dui, pretium nec purus rhoncus, aliquet imperdiet mauris. Sed euismod leo justo, nec gravida sem finibus a. Pellentesque sed nulla gravida mi consectetur tempus sit amet non neque. Suspendisse ornare tincidunt nisl eget tempus. Phasellus quis ligula sit amet enim euismod pellentesque a ut leo. Ut euismod nisi dui, vel mollis quam ultrices et. Proin non gravida odio. Donec non felis at nulla suscipit laoreet. Vivamus quis massa ut ex placerat congue a eget arcu. Pellentesque ante metus, sollicitudin sed lacus in, fringilla ullamcorper massa. Donec rhoncus massa egestas nisi dictum, vitae sodales nulla imperdiet.</p>
      <p>Suspendisse molestie lorem justo, sed porttitor nisl blandit sit amet. Ut pulvinar diam sit amet risus elementum feugiat. Sed ac arcu tincidunt, convallis velit ac, mollis lorem. Maecenas molestie volutpat quam vel tincidunt. Vestibulum consequat libero tortor, vel sagittis ante scelerisque at. Mauris ut tempor felis, quis posuere augue. Nullam interdum pretium placerat. In posuere felis et auctor pretium. Nam placerat tristique interdum. Suspendisse dolor quam, euismod ac nisl ut, porta interdum ante. Nunc vulputate eu eros vitae condimentum. Pellentesque maximus ultrices viverra. Donec at ultricies mauris. Maecenas nisi mi, fermentum non interdum vitae, venenatis eget turpis. Donec quis</p>
    </div>
    <div class="barcode-space"></div>

    <div class="spine">
      <div class="spine-title"><span class="line-one">NINE DAWNS AND</span><span class="line-two">FOUR DECADES</span></div>
      <div class="spine-author">IDRIS KAMAL-FARUQ</div>
    </div>

    <h1 class="front-title"><span class="line-one">Nine Dawns and</span><span class="line-two">Four Decades</span></h1>
    <p class="front-subtitle">The Dash and Endurance Path of Reaching Peak<br>Results</p>
    <p class="front-author">IDRIS KAMAL-FARUQ</p>
  </div>
</div>
</body>
</html>
```